Corvane Project Services - Flyer

Project Breif:
I need a single page A4 Capability Statement, which will be used to market our services to prospective clients, both in print and via email PDF.
It needs to look professional and should incorporate the elements I have uploaded into files, these include:
Capability Statement Text
Corvane Services Company Logo
Additional Logo’s (Tools We Use)
Glimmer Bay Pics can be cut into the page
I have included examples of capability statements as a guide to what i am looking for.
Regards
Derek
Engineering Consulting

```html
<!DOCTYPE html>
<html lang="en">
<head>
<meta charset="utf-8">
<title>Corvane Project Services – Capability Statement</title>
<link href="https://fonts.googleapis.com/css2?family=Oswald:wght@500;600&family=Lato:wght@400;700&display=swap" rel="stylesheet">
<style>
  :root{
    --blue:#2f63ad;
    --blue-dark:#1f4f94;
    --ink:#1d1d1f;
    --muted:#444;
    --rule:#cfd4db;
    --page:#f4f4f5;
    --backdrop:#a3a3a3;
  }
  *{margin:0;padding:0;box-sizing:border-box}
  html,body{width:1200px;height:1200px;overflow:hidden;background:var(--backdrop)}
  .flyer{position:absolute;left:211px;top:53px;width:778px;height:1093px;background:var(--page);
    box-shadow:0 4px 14px rgba(0,0,0,.25);font-family:'Lato',sans-serif;color:var(--ink);overflow:hidden}
  .header{height:141px;position:relative;background:#fff}
  .brand{position:absolute;left:22px;top:26px;width:170px;text-align:center}
  .brand-dot{width:44px;height:44px;border-radius:50%;background:var(--blue);margin:0 auto 10px}
  .brand-name{font-family:'Lato',sans-serif;font-weight:700;font-size:13px;color:var(--blue-dark);letter-spacing:.5px;text-transform:uppercase;line-height:1.25}
  .tagline{position:absolute;right:22px;top:49px;text-align:right;font-family:'Oswald',sans-serif;font-weight:600;
    font-size:21px;line-height:25px;color:var(--blue);text-transform:uppercase}
  .tagline-bar{position:absolute;right:0;top:42px;width:8px;height:65px;background:var(--blue)}
  .photo{height:267px;background:linear-gradient(120deg,#c9d8ea 0%,#eef3f9 35%,#ffffff 55%,#d5e1ee 80%,#b9cbe0 100%)}
  .band{height:88px;background:var(--blue);color:#fff;font-family:'Oswald',sans-serif;font-weight:500;
    font-size:22px;line-height:31px;padding:10px 22px;text-transform:uppercase;letter-spacing:-.2px}
  .intro{padding:26px 22px 0}
  .lead{color:var(--blue);font-weight:700;font-size:19.5px;line-height:25px;margin-bottom:22px}
  .intro p{font-size:19.5px;line-height:25px;margin-bottom:24px}
  .intro p.last{margin-bottom:12px}
  .rule{height:1px;background:var(--rule);margin:0 22px}
  .core{padding:20px 22px 0}
  .core h2{font-family:'Oswald',sans-serif;font-weight:500;font-size:24px;color:var(--blue);text-transform:uppercase;margin-bottom:14px}
  .cols{display:flex}
  .col{padding:0 0 0 2px}
  .col + .col{border-left:1px solid var(--rule);padding-left:14px}
  .col-plan{width:292px}.col-risk{width:280px}.col-cost{flex:1}
  .col h3{font-size:13.5px;font-weight:700;margin-bottom:6px}
  .col ul{list-style:none}
  .col li{font-size:12.3px;line-height:23.4px;color:var(--muted);position:relative;padding-left:22px}
  .col li::before{content:"";position:absolute;left:3px;top:8px;border-left:9px solid var(--blue);border-top:4px solid transparent;border-bottom:4px solid transparent}
  .footer{position:absolute;left:0;right:0;bottom:46px;height:40px;background:var(--blue);display:flex;align-items:center}
  .signature{position:absolute;left:22px;bottom:-20px;width:220px;height:80px;background:#fff;border:4px solid var(--blue);
    border-radius:8px;text-align:center;padding-top:6px}
  .signature .name{font-family:'Oswald',sans-serif;font-weight:600;font-size:31px;color:var(--blue);line-height:38px}
  .signature .role{font-family:'Oswald',sans-serif;font-weight:500;font-size:15px;color:var(--ink)}
  .contacts{margin-left:264px;display:flex;gap:20px;color:#fff;font-size:12.6px;align-items:center}
  .contact{display:flex;align-items:center;gap:7px}
  .contact svg{fill:none;stroke:#fff;stroke-width:1.6}
</style>
</head>
<body>
<main class="flyer">
  <header class="header">
    <div class="brand">
      <div class="brand-dot"></div>
      <div class="brand-name">Corvane Project Services</div>
    </div>
    <h1 class="tagline">Corvane Project Services Ltd. is a leading project<br>control consultancy based in Co Cork Ireland</h1>
    <div class="tagline-bar"></div>
  </header>

  <div class="photo" role="img" aria-label="Photo of colleagues reviewing project documents at a desk"></div>

  <div class="band">For over 20 years we have been helping our clients to deliver complex projects and programs throughout mainland Europe.</div>

  <section class="intro">
    <p class="lead">We are passionate about empower organisations to achieve their objectives, on time and on budget.</p>
    <p>We are continually innovating, evolving and learning, utilize the latest industry tools and techniques to deliver real value to our clients.</p>
    <p class="last">Our goal is to make successful project delivery more achievable and repeatable.</p>
  </section>
  <div class="rule"></div>

  <section class="core">
    <h2>Core Services:</h2>
    <div class="cols">
      <div class="col col-plan">
        <h3>Planning and Scheduling</h3>
        <ul>
          <li>Tender Planning</li>
          <li>Interactive Planning / Pull Planning</li>
          <li>EPCMV Planning &amp; Scheduling</li>
          <li>Schedule Earned Value Management</li>
          <li>Independent Schedule Quality Assessment</li>
          <li>Schedule Risk Analysis (Monte Carlo)</li>
          <li>Training</li>
        </ul>
      </div>
      <div class="col col-risk">
        <h3>Management of Risk</h3>
        <ul>
          <li>Risk Management Policies &amp; Procedures</li>
          <li>Risk Management Strategy</li>
          <li>Risk Registers</li>
          <li>Risk Improvement Planning</li>
          <li>Risk Response and Communication</li>
          <li>Risk Management Training</li>
        </ul>
      </div>
      <div class="col col-cost">
        <h3>Cost Control:</h3>
        <ul>
          <li>Estimating &amp; Forecasting</li>
          <li>Earned Value Analysis</li>
          <li>Progress Reporting</li>
          <li>Cost Risk Analysis</li>
        </ul>
      </div>
    </div>
  </section>

  <footer class="footer">
    <div class="signature">
      <div class="name">Derek Hartley</div>
      <div class="role">(Managing Director)</div>
    </div>
    <div class="contacts">
      <span class="contact"><svg width="10" height="17" viewBox="0 0 10 17"><rect x="1" y="1" width="8" height="15" rx="1.5"/></svg>+353 (0)870 415 926</span>
      <span class="contact"><svg width="20" height="13" viewBox="0 0 20 13"><rect x="1" y="1" width="18" height="11"/><path d="M1 1l9 6 9-6"/></svg>info@corvaneservices.ie</span>
      <span class="contact"><svg width="17" height="15" viewBox="0 0 17 15"><rect x="1" y="3" width="15" height="11" rx="1"/><path d="M4 3V1h9v2"/></svg>www.corvaneservices.ie</span>
    </div>
  </footer>
</main>
</body>
</html>
```